CD/Album cover design - Ember & Tide

Hi, I need an album cover designed. The name of the album is called 'Ember and Tide' Not 100% sure of the concept, but using colored lines, Geometrical shapes etc, angles and maybe a circle or triangle in the middle. A cross between, Velvet Harbor ,Paper towns of the rain (But dont make it look like this old look album) , 80s retro synthwave album covers, perhaps with neon color lines but not all of it etc. Have it modern looking . My name on cover and album name. Back, songs etc and info details. The style of the music is EDM meets guitar. Trap, house music and guitar as the main theme instrument, with sythns. Keep it relatively simple looking, and maybe have the background white,, but with the color designs, wording etc colors. or if you feel it would look better another way, just use your own judgement and creativity. Ve attached a couple of Pics. The Velvet Hrabor pic , more of concept. The retro one... I like the design in the middle but not wording at the top. The QJ crest one, I like how the wording is in the middle of circle. So a combination of these, with geometrical lines, colors, etc. I am also open to a completely new idea that you think would look awesome. The album is really combining Guitar with House/Tap EDM music, and the concept Ember and Tide - The beginning and end (Of everything) Thanks
Target Market(s)
EDM , Guitarists
Industry/Entity Type
Music, EDM, Guitar Instrumental
Look and feel

```html
<!DOCTYPE html>
<html lang="en">
<head>
<meta charset="utf-8">
<title>Ember and Tide – Album Cover</title>
<link rel="stylesheet" href="https://fonts.googleapis.com/css2?family=DM+Serif+Display&family=Great+Vibes&display=swap">
<style>
  :root {
    --night: #1f0048;
    --plum: #4a0a48;
    --crimson: #b81c4c;
    --ocean: #1c5fae;
    --script-red: #f0284a;
  }
  html, body {
    margin: 0;
    padding: 0;
    width: 1200px;
    height: 1200px;
    overflow: hidden;
    background: #ffffff;
  }
  .album-cover {
    display: block;
    width: 1200px;
    height: 1200px;
  }
  .title-word {
    font-family: "DM Serif Display", Georgia, serif;
  }
  .title-joiner {
    font-family: "Great Vibes", cursive;
  }
</style>
</head>
<body>
<svg class="album-cover" viewBox="0 0 1200 1200" xmlns="http://www.w3.org/2000/svg" role="img" aria-label="Ember and Tide album cover">
  <defs>
    <linearGradient id="backdrop-fill" x1="0" y1="0" x2="0" y2="1">
      <stop offset="0" stop-color="var(--night)"/>
      <stop offset="0.35" stop-color="var(--night)"/>
      <stop offset="0.6" stop-color="var(--plum)"/>
      <stop offset="0.85" stop-color="var(--crimson)"/>
      <stop offset="1" stop-color="var(--ocean)"/>
    </linearGradient>
    <linearGradient id="ring" x1="0" y1="0" x2="1" y2="1">
      <stop offset="0" stop-color="#c9c9cc"/>
      <stop offset="0.35" stop-color="#ffffff"/>
      <stop offset="0.7" stop-color="#a9a9ad"/>
      <stop offset="1" stop-color="#f2f2f2"/>
    </linearGradient>
    <linearGradient id="lens" x1="0" y1="0" x2="0" y2="1">
      <stop offset="0" stop-color="#a897ab"/>
      <stop offset="0.45" stop-color="#5e3f5e"/>
      <stop offset="0.75" stop-color="#3a3350"/>
      <stop offset="1" stop-color="#2f7a52"/>
    </linearGradient>
    <linearGradient id="silver" x1="0" y1="0" x2="0" y2="1">
      <stop offset="0" stop-color="#ffffff"/>
      <stop offset="0.55" stop-color="#e4e4e6"/>
      <stop offset="1" stop-color="#9a9a9e"/>
    </linearGradient>
    <filter id="lift" x="-20%" y="-20%" width="140%" height="160%">
      <feDropShadow dx="4" dy="12" stdDeviation="7" flood-color="#000" flood-opacity="0.55"/>
    </filter>
    <filter id="ring-shadow" x="-20%" y="-20%" width="140%" height="140%">
      <feDropShadow dx="0" dy="6" stdDeviation="10" flood-color="#000" flood-opacity="0.45"/>
    </filter>
  </defs>

  <rect class="backdrop" width="1200" height="1200" fill="url(#backdrop-fill)" role="img" aria-label="Abstract background artwork with colour bands and soft glows in purple, crimson and blue"/>

  <g class="center-disc">
    <circle cx="600" cy="572" r="399" fill="url(#ring)" filter="url(#ring-shadow)"/>
    <circle cx="600" cy="572" r="386" fill="url(#lens)"/>
  </g>

  <g class="title">
    <text class="title-word" x="600" y="490" text-anchor="middle" font-size="148" fill="url(#silver)" filter="url(#lift)" textLength="510" lengthAdjust="spacingAndGlyphs">Ember</text>
    <text class="title-word" x="600" y="700" text-anchor="middle" font-size="148" fill="url(#silver)" filter="url(#lift)" textLength="420" lengthAdjust="spacingAndGlyphs">Tide</text>
    <text class="title-joiner" x="614" y="572" text-anchor="middle" font-size="88" fill="var(--script-red)">And</text>
  </g>
</svg>
</body>
</html>
```